Contractor Plan "B"/Getting Screwed?/Something Useful

We are sending out a series of postcards to a group of local contractors.

The first in the series is: Plan B: Pink Bubble Wrap. Plan A is to buy insurance from my agency. This will be printed, front and back on card stock. We will then glue a piece of bubble wrap to the card and place it in an envelope for delivery.

The second card will be along the same lines but will ask if the client is getting screwed by his current Insurance Company. We will glue a screw in the middle of the card and place the card in an envelope for delivery. On the bottom of we might tell them to call us to get unscrewed.

The third card will follow those lines but say something like: We sent you bubble wrap for your Plan B and you didn't call. Then we sent you something funny but you didn't call. We decided to send you something useful so you might call now! With this card, we are going to send a carpenter pencil.

I am attaching a rough outline of my sketch design for the first card so you will have basic information we will need such as phone number and coverages we offer. If you feel like there is too much info for the size of the card, we can leave some off. I just want the phone to ring! Also, feel free to adjust the wording to make it work better...creative design is not my strong suit!!

I would like for all three cards to be designed. Each can have the same backside. Also, please keep in mind, this is not a postcard so you don't have to leave the blanks on the back for addressing. Each will be mailed in an envelope.

I have also uploaded my logo file as we have recently redone the logo.

Here is more guidance on the project: The cards are going to be 10 cm wide and 23 cm tall. I have added more wording in the brief. Also, I attached a word doc with a good idea of what to use for wording. Basically I want the following idea: Card 1: At top of card - Plan B: Pink Bubble Wrap Below the bubble wrap - Plan A: Call us so you don't have to use Pink Bubble Wrap Card 2: At top of card - Getting Screwed? Is your current agent taking you for granted? Below the area where we are going to glue a screw - Get unscrewed, Call us! Card 3: At top of card - We have the sharpest pencil in town! We will leave space for a carpenter pencil to be attached tot he card. On the other side of the open space - Call us today for the best rates on your insurance!

Please review the attached word doc for an idea of what to put on the back of the card. To be clear, we need three designs for the front of the card and can probably use just one design for the back of all three. If you think we need to have a different design for the back of each, I would like to see your ideas. Thank you for your hard work on these!

Reason: Hi, I am extending the time as I am expecting a few more submissions. Thank you!

Target Market(s)

We are targeting both contractors and truckers with this campaign.

Industry/Entity Type

Insurance

Requirements
Must have
• Clever wording. It needs to be a call to action and doesn't need to have too many specifics.

We also have to have space in the middle to glue the bubble wrap on the first card, the screw in the second and attach the pencil in the third.

```html
<!DOCTYPE html>
<html lang="en">
<head>
<meta charset="utf-8">
<title>Sharpest Pencil in Town – Card</title>
<link rel="stylesheet" href="https://fonts.googleapis.com/css2?family=Arimo:wght@400;700&display=swap">
<style>
  :root {
    --card-green: #33e61e;
    --ink-white: #ffffff;
  }
  html, body {
    margin: 0;
    padding: 0;
    width: 1200px;
    height: 2755px;
    overflow: hidden;
    background: var(--card-green);
  }
  .card {
    position: relative;
    width: 1200px;
    height: 2755px;
    background: var(--card-green);
    color: var(--ink-white);
    font-family: "Arimo", Arial, sans-serif;
    text-align: center;
  }
  .headline {
    position: absolute;
    top: 110px;
    left: 0;
    width: 100%;
    margin: 0;
    font-weight: 700;
    line-height: 1;
    letter-spacing: -1px;
  }
  .headline span { display: block; }
  .headline .line-small { font-size: 96px; }
  .headline .line-big { font-size: 160px; margin-top: 6px; letter-spacing: -2px; }
  .headline .line-mid { font-size: 100px; margin-top: 10px; }

  .story {
    position: absolute;
    top: 570px;
    left: 100px;
    width: 1000px;
    font-weight: 400;
    font-size: 58px;
    line-height: 80px;
  }
  .story p { margin: 0 0 62px; }

  .pencil-spot {
    position: absolute;
    top: 1347px;
    left: 276px;
    width: 648px;
    height: 67px;
  }

  .call-to-action {
    position: absolute;
    top: 1525px;
    left: 0;
    width: 100%;
    margin: 0;
    font-weight: 400;
    font-size: 84px;
    line-height: 98px;
  }
  .phone {
    position: absolute;
    top: 1790px;
    left: 0;
    width: 100%;
    margin: 0;
    font-weight: 700;
    font-size: 138px;
    line-height: 1;
    letter-spacing: -1px;
  }
  .brand-name {
    position: absolute;
    top: 2420px;
    left: 0;
    width: 100%;
    margin: 0;
    font-weight: 700;
    font-size: 72px;
    line-height: 1;
    color: var(--ink-white);
  }
</style>
</head>
<body>
  <main class="card">
    <h1 class="headline">
      <span class="line-small">WE HAVE THE</span>
      <span class="line-big">SHARPEST</span>
      <span class="line-mid">PENCIL IN TOWN!</span>
    </h1>

    <div class="story">
      <p>We sent you a great Plan B idea<br>and we didn’t hear from you.</p>
      <p>We sent you something funny<br>and we didn’t hear from you.</p>
      <p>Now we are sending something<br>useful, hoping you call!</p>
    </div>

    <svg class="pencil-spot" viewBox="0 0 648 67" role="img" aria-label="Carpenter pencil attached here">
      <rect x="0" y="0" width="648" height="67" fill="#ffffff"/>
    </svg>

    <p class="call-to-action">Call us for the best rate<br>on your insurance!</p>
    <p class="phone">281-555-0147</p>

    <p class="brand-name">LONE OAK INSURANCE</p>
  </main>
</body>
</html>
```